Pellworth International needs a book cover

I am self publishing a book titles entitled, Quiet Threads Between Birth and Nurturing. Paperfield Press is ready to do the print, but I did not like their design. I am attaching the picture I want on the front.

Hello all - Thank you all for your beautiful designs.  I am closing this project in 24 hours. I will be making my final selection then.  I apologize for closing earlier than my deadline.  This is my first project and I have learned a lot:)  I will be back with more projects!

```html
<!DOCTYPE html>
<html lang="en">
<head>
<meta charset="utf-8">
<title>Quiet Threads Between Birth and Nurturing – Book Cover</title>
<link rel="stylesheet" href="https://fonts.googleapis.com/css2?family=Great+Vibes&family=Parisienne&family=Cinzel:wght@400&family=Open+Sans:wght@400;700&display=swap">
<style>
  :root {
    --stage: #d8d2c8;
    --back-black: #0b0a09;
    --back-glow: #2a2520;
    --gold-light: #ffd36a;
    --gold: #e7a52a;
    --gold-deep: #a8620f;
    --body-orange: #e8a23a;
    --body-cream: #f1e2c4;
    --spine-light: #ecebe8;
    --spine-mid: #c9c7c2;
    --spine-ink: #8a6a3a;
    --photo-light: #e9e7e3;
    --photo-mid: #a9a6a0;
    --photo-dark: #5d5a55;
    --author-ink: #141210;
    --white: #ffffff;
  }
  * { margin: 0; padding: 0; box-sizing: border-box; }
  html, body { width: 1200px; height: 900px; overflow: hidden; }
  body { background: var(--stage); position: relative; font-family: "Open Sans", sans-serif; }

  .book-wrap {
    position: absolute; left: 21px; top: 100px;
    width: 1158px; height: 700px; display: flex;
    box-shadow: 0 18px 40px rgba(0,0,0,.35);
  }

  /* Back cover */
  .back-cover {
    width: 544px; height: 700px; position: relative;
    background: var(--back-black); overflow: hidden; color: var(--body-orange);
  }
  .back-photo {
    position: absolute; left: 60px; top: 120px; width: 430px; height: 460px;
    background: radial-gradient(ellipse at 45% 45%, var(--back-glow) 0%, rgba(20,18,16,.6) 45%, transparent 72%);
  }
  .back-title { position: absolute; top: 40px; width: 100%; text-align: center; }
  .back-content { position: absolute; top: 205px; left: 50px; right: 50px; text-align: center; }
  .back-blurb { font-size: 12px; line-height: 1.45; color: var(--body-orange); margin-bottom: 12px; }
  .back-blurb strong { color: var(--gold); }
  .back-quote {
    font-family: "Parisienne", cursive; font-size: 24px; line-height: 1.5;
    color: var(--gold); margin: 34px 0 70px;
  }
  .back-bio { font-size: 12.5px; line-height: 1.45; color: var(--body-orange); }

  .script-title {
    font-family: "Great Vibes", cursive; line-height: .85;
    background: linear-gradient(180deg, var(--gold-light) 0%, var(--gold) 55%, var(--gold-deep) 100%);
    -webkit-background-clip: text; background-clip: text; color: transparent;
  }
  .script-sub { font-family: "Parisienne", cursive; color: var(--body-cream); }
  .back-title .script-title { font-size: 46px; }
  .back-title .script-title .line-2 { display: block; margin-left: 90px; }
  .back-title .script-sub { font-size: 19px; margin-top: 4px; }

  /* Spine */
  .spine {
    width: 70px; height: 700px; position: relative;
    background: linear-gradient(90deg, var(--spine-mid) 0%, var(--spine-light) 40%, var(--spine-light) 70%, var(--spine-mid) 100%);
  }
  .spine-text {
    position: absolute; top: 30px; left: 50%; width: 640px;
    transform-origin: 0 0; transform: rotate(90deg) translateY(-50%);
    display: flex; align-items: baseline; gap: 18px; color: var(--spine-ink); white-space: nowrap;
  }
  .spine-title { font-family: "Cinzel", serif; font-size: 21px; }
  .spine-sub { font-family: "Parisienne", cursive; font-size: 20px; }
  .spine-author { font-family: "Cinzel", serif; font-size: 16px; margin-left: auto; letter-spacing: 1px; }

  /* Front cover */
  .front-cover { width: 544px; height: 700px; position: relative; overflow: hidden; }
  .front-photo {
    position: absolute; inset: 0;
    background:
      radial-gradient(ellipse at 70% 55%, var(--photo-light) 0%, transparent 40%),
      radial-gradient(ellipse at 35% 45%, var(--photo-mid) 0%, transparent 45%),
      linear-gradient(160deg, var(--photo-mid) 0%, var(--photo-light) 45%, var(--photo-dark) 80%, var(--photo-light) 100%);
  }
  .front-title { position: absolute; top: 50px; left: 28px; right: 20px; }
  .front-title .script-title {
    font-size: 98px; filter: drop-shadow(2px 3px 2px rgba(0,0,0,.45));
  }
  .front-title .line-2 { display: block; margin-left: 120px; margin-top: -6px; }
  .front-title .script-sub {
    font-size: 30px; margin-left: 100px; margin-top: 4px; color: var(--white);
    text-shadow: 1px 1px 3px rgba(0,0,0,.7);
  }
  .front-author {
    position: absolute; right: 34px; bottom: 62px;
    font-family: "Cinzel", serif; font-size: 30px; color: var(--author-ink); letter-spacing: .5px;
  }
</style>
</head>
<body>
  <main class="book-wrap">
    <section class="back-cover">
      <div class="back-photo" role="img" aria-label="Faint dark photograph of a mother holding her newborn"></div>
      <header class="back-title">
        <div class="script-title"><span class="line-1">Quiet</span><span class="line-2">Threads</span></div>
        <div class="script-sub">between birth &amp; nurturing</div>
      </header>
      <div class="back-content">
        <p class="back-blurb">When we grow older and learn more about science and the things we can easily understand and touch, we stray from a spiritual connection. This book is about the journey back in an intentional and purposeful way, using pregnancy and motherhood as a vehicle to go deeper.</p>
        <p class="back-blurb"><strong>Quiet Threads Between Birth and Nurturing</strong> is a women's journey as we go deeper into our soul to love ourselves unconditionally each moment. Only then can we begin to love all others with the same unconditional love.</p>
        <p class="back-quote">“Mothers are the spiritual glue<br>that holds a family together.”</p>
        <p class="back-bio">MARIAN ELSWORTH is the proud mother of three amazing and beautiful children, Hazel, Jonah and Elise. Born and raised in Brackenford, Maine, Marian now resides in Hollins Ridge, Virginia with her fiancé, Jude and youngest daughter, Elise. She lives life fully as a passionate educator, engineer and writer.</p>
      </div>
    </section>

    <section class="spine">
      <div class="spine-text">
        <span class="spine-title">Quiet Threads</span>
        <span class="spine-sub">between birth &amp; nurturing</span>
        <span class="spine-author">MARIAN ELSWORTH</span>
      </div>
    </section>

    <section class="front-cover">
      <div class="front-photo" role="img" aria-label="Black and white photograph of a pregnant mother with her young son and daughter, with baby's breath flowers"></div>
      <header class="front-title">
        <h1 class="script-title"><span class="line-1">Quiet</span><span class="line-2">Threads</span></h1>
        <div class="script-sub">between birth &amp; nurturing</div>
      </header>
      <p class="front-author">MARIAN ELSWORTH</p>
    </section>
  </main>
</body>
</html>
```